TELVIRA Web Page

We need a corporate web site for a new company TELVIRA Corporation. TELVIRA is a technology company that has developed a new virtualization solution for corporate applications. Our target customers are IT professionals. We have a logo, which we will provide.

Final design should communicate: innovation, stability, professionalism

Industry/Entity Type

It Company

```html
<!DOCTYPE html>
<html lang="en">
<head>
<meta charset="utf-8">
<title>TELVIRA Corporation</title>
<link href="https://fonts.googleapis.com/css2?family=Open+Sans:wght@400;600;700&family=Pontano+Sans&display=swap" rel="stylesheet">
<style>
:root{
  --navy:#0e1a38;
  --navy-soft:rgba(20,36,70,.82);
  --yellow:#ffd800;
  --ink:#1b2540;
  --text:#6b6f78;
  --light:#efefef;
  --rule:#d9dbe0;
  --tab-grey:#b9bcc2;
  --white:#fff;
}
*{box-sizing:border-box;margin:0;padding:0}
html,body{width:1200px;height:2497px;overflow:hidden;background:var(--white)}
body{position:relative;font-family:"Open Sans",sans-serif;color:var(--text)}
.abs{position:absolute}
.display{font-family:"Pontano Sans","Open Sans",sans-serif}

/* hero */
.hero{left:0;top:0;width:1200px;height:749px;
  background:linear-gradient(100deg,#f3f4f6 0%,#dfe2e6 30%,#c4c8cf 55%,#a9acb3 75%,#cdd0d5 100%)}
.brand{left:77px;top:24px;display:flex;align-items:center;gap:14px}
.brand-mark{width:64px;height:64px;background:var(--yellow)}
.brand-name{font-size:37px;color:var(--ink)}
.social{top:62px;right:77px;display:flex;gap:4px}
.social span{height:36px;padding:0 8px;background:var(--navy);color:var(--white);font-size:12px;font-weight:600;line-height:36px}
.nav{left:77px;top:133px;width:1046px;height:78px;background:var(--navy);display:flex;box-shadow:0 4px 8px rgba(0,0,0,.25)}
.nav a{color:var(--white);text-decoration:none;font-size:16px;display:flex;align-items:center;justify-content:center;border-right:1px solid #26324e}
.nav a.active{background:var(--yellow);color:var(--ink)}
.tagline{left:77px;top:404px;width:248px;height:49px;background:var(--white);color:var(--ink);font-weight:600;font-size:17px;line-height:49px;padding-left:16px}
.hero-card{left:77px;top:459px;width:452px;height:158px;background:var(--navy-soft);color:#eef0f4;font-size:17px;line-height:26px;padding:30px 20px}
.hero-plus{left:494px;top:582px;width:35px;height:35px;background:var(--yellow);color:var(--ink);font-size:24px;text-align:center;line-height:35px}
.dots{left:500px;top:712px;display:flex;gap:6px}
.dots i{width:22px;height:22px;background:var(--white);border:2px solid #555;display:block}
.dots i.on{background:#555}

/* features */
.feature{width:260px;text-align:center}
.feature .ring{width:188px;height:188px;border-radius:50%;background:var(--light);margin:0 auto;display:flex;align-items:center;justify-content:center}
.feature .disc{width:150px;height:150px;border-radius:50%;background:var(--white);display:flex;align-items:center;justify-content:center}
.feature h3{margin-top:42px;padding-top:10px;border-top:1px solid var(--rule);width:180px;margin-left:40px;margin-right:40px;font-size:25px;font-weight:400;color:var(--ink)}
.feature p{margin-top:14px;font-size:14.5px;line-height:25px}
.divider{left:77px;top:1247px;width:1046px;height:3px;background:var(--navy)}

/* section bars */
.bar{height:50px;display:flex;background:repeating-linear-gradient(45deg,#eceef1 0 2px,#fff 2px 4px)}
.bar .label{background:var(--navy);color:var(--white);font-size:17px;padding:0 22px;line-height:50px}
.bar .tab{background:var(--tab-grey);color:var(--white);font-size:15px;font-weight:600;padding:0 26px;line-height:50px}
.bar .ctrls{margin-left:auto;display:flex;gap:2px}
.bar .ctrls span{width:36px;height:50px;background:var(--navy);color:var(--white);font-size:20px;text-align:center;line-height:48px}

/* services */
.service{width:244px;text-align:center;border-bottom:3px solid var(--navy);padding-bottom:10px}
.service .photo{height:167px}
.service h4{margin-top:14px;font-size:20px;font-weight:600;color:var(--ink)}
.service small{display:block;font-size:14px;margin-top:2px}

/* posts */
.post{left:77px;width:512px;display:flex;gap:14px;border-bottom:1px solid var(--rule);padding-bottom:14px}
.date{width:73px;height:91px;background:var(--navy);color:var(--white);text-align:center;flex:none}
.date b{display:block;font-weight:400;font-size:33px;line-height:54px}
.date span{font-size:18px}
.post h5{font-size:24px;font-weight:400;color:var(--ink);line-height:31px}
.post p{font-size:14px;line-height:22px}

.quote{left:611px;top:1769px;width:512px;height:158px;background:#f2f3f5;border:1px solid #e2e4e8;padding:24px 26px;font-size:14.5px;line-height:23px}
.quote p+p{margin-top:16px}
.cite{left:611px;top:1930px;width:450px;text-align:right;font-size:15px}
.cite b{color:#444}

/* footer */
.foot-rule{left:0;top:2050px;width:1200px;height:5px;background:var(--navy)}
.col{width:244px}
.col h6{font-size:24px;font-weight:400;color:var(--ink);padding-bottom:12px;border-bottom:2px solid var(--rule)}
.col p{margin-top:20px;font-size:14.5px;line-height:24px}
.links{list-style:none;margin-top:16px}
.links li{font-size:14.5px;line-height:32px;color:#333;padding-left:28px;position:relative}
.links li svg{position:absolute;left:0;top:10px}
.thumbs{margin-top:16px;display:grid;grid-template-columns:repeat(3,67px);gap:6px}
.thumbs div{height:67px}
.tweet{margin-top:20px;padding-left:28px;position:relative;font-size:14.5px;line-height:23px;color:#444}
.tweet::before{content:"";position:absolute;left:2px;top:6px;width:14px;height:14px;border-radius:50%;background:var(--navy)}
.tweet em{font-style:normal;color:#999}
.tweet small{font-size:12px;color:#666}
.foot-bottom{left:77px;top:2427px;width:1046px;border-top:1px solid #e5e6ea;padding-top:20px;font-size:13px;color:#888}
</style>
</head>
<body>

<div class="abs hero" role="img" aria-label="Photo of a smiling businessman in a meeting room with colleagues at a presentation"></div>

<div class="abs brand"><span class="brand-mark"></span><span class="brand-name display">TELVIRA Corporation</span></div>
<div class="abs social"><span>RSS</span><span>Linkora</span><span>Facenet</span><span>Chirpa</span></div>

<nav class="abs nav">
  <a class="active" style="width:135px">Home</a>
  <a style="width:158px">About Us</a>
  <a style="width:150px">Services</a>
  <a style="width:150px">Support</a>
  <a style="width:139px">Clients</a>
  <a style="width:120px">FAQ</a>
  <a style="width:194px;border-right:0">Contact Us</a>
</nav>

<div class="abs tagline">We are smart, creative...!</div>
<div class="abs hero-card">Nemo enim ipsam voluptatem, quia voluptas sit, aspernatur aut odit aut fugit, sed quia consequuntur magn.</div>
<div class="abs hero-plus">+</div>
<div class="abs dots"><i style="border:0;background:none;color:#fff">›</i><i class="on"></i><i></i><i></i><i></i><i></i><i></i></div>

<div class="abs feature" style="left:66px;top:778px">
  <div class="ring"><div class="disc">
    <svg width="66" height="72" viewBox="0 0 66 72"><rect x="3" y="10" width="60" height="58" rx="6" fill="none" stroke="#0e1a38" stroke-width="6"/><rect x="3" y="10" width="60" height="14" fill="#0e1a38"/><rect x="14" y="2" width="6" height="14" fill="#0e1a38"/><rect x="46" y="2" width="6" height="14" fill="#0e1a38"/><g fill="#0e1a38"><rect x="12" y="30" width="9" height="8"/><rect x="24" y="30" width="9" height="8"/><rect x="36" y="30" width="9" height="8"/><rect x="48" y="30" width="6" height="8"/><rect x="12" y="42" width="9" height="8"/><rect x="24" y="42" width="9" height="8"/><rect x="36" y="42" width="9" height="8"/><rect x="48" y="42" width="6" height="8"/><rect x="12" y="54" width="9" height="8"/><rect x="24" y="54" width="9" height="8"/><rect x="36" y="54" width="9" height="8"/></g></svg>
  </div></div>
  <h3 class="display">Lorem Ipsum</h3>
  <p>Nemo enim ipsam voluptatem, quia voluptas sit, aspernatur aut odit aut fugit, sed quia consequ untur consequuntur magni dolores eos.</p>
</div>
<div class="abs feature" style="left:334px;top:778px">
  <div class="ring"><div class="disc">
    <svg width="64" height="70" viewBox="0 0 64 70" fill="#0e1a38"><circle cx="32" cy="12" r="10"/><rect x="20" y="25" width="24" height="38" rx="8"/><circle cx="11" cy="20" r="7"/><rect x="2" y="30" width="16" height="28" rx="6"/><circle cx="53" cy="20" r="7"/><rect x="46" y="30" width="16" height="28" rx="6"/></svg>
  </div></div>
  <h3 class="display">Lorem Ipsum</h3>
  <p>Nemo enim ipsam voluptatem, quia voluptas sit, aspernatur aut odit aut fugit, sed quia consequ untur consequuntur magni dolores eos.</p>
</div>
<div class="abs feature" style="left:602px;top:778px">
  <div class="ring"><div class="disc">
    <svg width="44" height="76" viewBox="0 0 44 76" fill="#0e1a38"><path d="M12 2h16l-4 10H16z"/><path d="M15 14h10l8 44-13 16-12-16z"/><path d="M30 18l12 10-6 4z"/></svg>
  </div></div>
  <h3 class="display">Lorem Ipsum</h3>
  <p>Nemo enim ipsam voluptatem, quia voluptas sit, aspernatur aut odit aut fugit, sed quia consequ untur consequuntur magni dolores eos.</p>
</div>
<div class="abs feature" style="left:868px;top:778px">
  <div class="ring"><div class="disc">
    <svg width="76" height="70" viewBox="0 0 76 70"><g fill="none" stroke="#0e1a38" stroke-width="4"><path d="M22 4c-5 4 5 8 0 12s5 8 0 10"/><path d="M38 4c-5 4 5 8 0 12s5 8 0 10"/><path d="M54 4c-5 4 5 8 0 12s5 8 0 10"/></g><rect x="0" y="32" width="76" height="6" fill="#0e1a38"/><path d="M4 40h68c0 14-14 22-34 22S4 54 4 40z" fill="#0e1a38"/><rect x="22" y="62" width="32" height="6" fill="#0e1a38"/></svg>
  </div></div>
  <h3 class="display">Lorem Ipsum</h3>
  <p>Nemo enim ipsam voluptatem, quia voluptas sit, aspernatur aut odit aut fugit, sed quia consequ untur consequuntur magni dolores eos.</p>
</div>

<div class="abs divider"></div>

<div class="abs bar" style="left:77px;top:1290px;width:1046px"><span class="label">Our Services</span><span class="ctrls"><span>▪</span><span>‹</span><span>›</span></span></div>

<div class="abs service" style="left:77px;top:1371px"><div class="photo" role="img" aria-label="Photo of a business team seated around a meeting table" style="background:linear-gradient(#e9ebee,#6f7480)"></div><h4>Lorem ipsum dolor</h4><small>Nullam enim leo</small></div>
<div class="abs service" style="left:343px;top:1371px"><div class="photo" role="img" aria-label="Photo of a businesswoman working at a computer" style="background:linear-gradient(#f1f2f4,#7b8089)"></div><h4>Lorem ipsum dolor</h4><small>Nullam enim leo</small></div>
<div class="abs service" style="left:611px;top:1371px"><div class="photo" role="img" aria-label="Photo of a presenter at a whiteboard with a seated team" style="background:linear-gradient(#eceef0,#858a93)"></div><h4>Lorem ipsum dolor</h4><small>Nullam enim leo</small></div>
<div class="abs service" style="left:879px;top:1371px"><div class="photo" role="img" aria-label="Photo of colleagues reviewing work on a laptop" style="background:linear-gradient(#e6e7ea,#4d525c)"></div><h4>Lorem ipsum dolor</h4><small>Nullam enim leo</small></div>

<div class="abs bar" style="left:77px;top:1686px;width:512px"><span class="label">Recent Posts</span><span class="ctrls"><span>▪</span><span>‹</span><span>›</span></span></div>
<div class="abs bar" style="left:611px;top:1686px;width:512px"><span class="label" style="font-size:15px;font-weight:600">Testimonials</span><span class="tab">Clients</span><span class="ctrls"><span>▪</span><span>‹</span><span>›</span></span></div>

<div class="abs post" style="top:1769px"><div class="date"><b>05</b><span>mar</span></div><div><h5 class="display">Breakpoints For Your Responsive</h5><p>There are several tactics for deciding where to put breakpoints in . There is the rusty idea that they should.</p></div></div>
<div class="abs post" style="top:1889px"><div class="date"><b>06</b><span>mar</span></div><div><h5 class="display">Logical Breakpoints For Your Responsive</h5><p>There are several tactics for deciding where to put breakpoints in . There is the rusty idea that they should.</p></div></div>

<div class="abs quote"><p>Id elit non mi porta gravida at eget metus. Fusce dapibus, tellus ac cursus commodo, tellus ac cursus commodo, tortor mauris condimentum nibh. Imt fermentum massa justo sit amet risus.</p><p>Atiam porta sem malesuada magna mollis euismod.</p></div>
<div class="abs cite"><b>John doe</b>, General Manager</div>

<div class="abs foot-rule"></div>

<div class="abs col" style="left:77px;top:2085px"><h6 class="display">TELVIRA</h6><p>Nemo enim ipsam voluptatem, quia voluptas sit, aspernatur aut odit aut fugit, sed quia conse quuntur consequun. turmagni dolores eos.</p><p>Bemo enim ipsam voluptatem, quia voluptas sit, aspernatur aut odit aut fugit.</p></div>
<div class="abs col" style="left:343px;top:2085px"><h6 class="display">About &amp; Legal</h6>
  <ul class="links">
    <li><svg width="14" height="12" viewBox="0 0 14 12"><path d="M1 6l4 4 8-9" fill="none" stroke="#0e1a38" stroke-width="3"/></svg>Asure core Philosophy</li>
    <li><svg width="14" height="12" viewBox="0 0 14 12"><path d="M1 6l4 4 8-9" fill="none" stroke="#0e1a38" stroke-width="3"/></svg>Projects we did so for</li>
    <li><svg width="14" height="12" viewBox="0 0 14 12"><path d="M1 6l4 4 8-9" fill="none" stroke="#0e1a38" stroke-width="3"/></svg>Terms &amp; Conditions</li>
    <li><svg width="14" height="12" viewBox="0 0 14 12"><path d="M1 6l4 4 8-9" fill="none" stroke="#0e1a38" stroke-width="3"/></svg>Privacy &amp; Security</li>
    <li><svg width="14" height="12" viewBox="0 0 14 12"><path d="M1 6l4 4 8-9" fill="none" stroke="#0e1a38" stroke-width="3"/></svg>Content Copyrights</li>
    <li style="line-height:26px;margin-top:4px"><svg width="14" height="12" viewBox="0 0 14 12" style="top:7px"><path d="M1 6l4 4 8-9" fill="none" stroke="#0e1a38" stroke-width="3"/></svg>Registration and Memberships</li>
  </ul>
</div>
<div class="abs col" style="left:611px;top:2085px"><h6 class="display">Daily Stils</h6>
  <div class="thumbs" role="img" aria-label="Grid of small team and office photos">
    <div style="background:#8a9099"></div><div style="background:#5d6470"></div><div style="background:#6c6f74"></div>
    <div style="background:#7d8792"></div><div style="background:#4f5a52"></div><div style="background:#3e4247"></div>
    <div style="background:#7a5c45"></div><div style="background:#6e7378"></div>
  </div>
</div>
<div class="abs col" style="left:879px;top:2085px"><h6 class="display">Latest Tweets</h6>
  <div class="tweet"><em>@rovenhal</em> you have been replied to. Please also check your spam folder. Thanks ^TC <small>25/04/2013 21:50:12</small></div>
  <div class="tweet"><em>@kestrel_note</em> ???????! (Thanks!) ^DZ <small>25/04/2013 20:12:39</small></div>
</div>

<div class="abs foot-bottom">© 2013 TELVIRA Corporation . All Rights Reserved</div>

</body>
</html>
```